依頼詳細
チラシを持参してもらったお客様限定のお試し価格の案内チラシを作成したいと思います。
普段のお客様ですと、お店の高級感から敷居が高いように感じられがちですが、
今回は、少しライトな層を狙えるようなイメージを持っています。
記載項目
◆焼肉バー ミヨコ

・ぐるめ帳ページ
https://gurumecho.example/aichi/B4812/B481207/58194630/

・Picstream
https://www.picstream.example/miyoko_yakiniku_bar/
サイズ
A5
ページ数
片面
希望イメージ
シンプル 複雑
単色 カラフル
暗い 明るい
日常 高級
遊び心 厳粛
未来的 伝統的
女性的 男性的
希望する色
黄・オレンジ系、無彩色系
納品ファイル
• 高解像度JPG (.jpg)
• イラストレーター形式 (.ai)
補足説明

```html
<!DOCTYPE html>
<html lang="ja">
<head>
<meta charset="UTF-8">
<title>焼肉BAR MIYOKO お試しコース</title>
<link href="https://fonts.googleapis.com/css2?family=Shippori+Mincho:wght@500;700;800&display=swap" rel="stylesheet">
<style>
  :root {
    --bg: #1d1d1d;
    --gold: #c8b37d;
    --white: #f4f1ea;
    --line: #6e6248;
  }
  * { margin: 0; padding: 0; box-sizing: border-box; }
  html, body { width: 844px; height: 1200px; overflow: hidden; background: var(--bg); }
  body { font-family: "Shippori Mincho", serif; color: var(--white); }
  .flyer { position: relative; width: 844px; height: 1200px; background: var(--bg); overflow: hidden; }

  .hero-photo {
    position: absolute; left: 0; top: 0; width: 844px; height: 720px;
    background:
      linear-gradient(180deg, rgba(29,29,29,0.55) 0%, rgba(29,29,29,0.15) 35%, rgba(29,29,29,0.1) 60%, var(--bg) 100%),
      radial-gradient(ellipse at 45% 45%, #9a4a42 0%, #6b2d2a 35%, #3a2421 70%, #1d1d1d 100%);
  }

  .headline { position: absolute; writing-mode: vertical-rl; font-weight: 800; color: var(--white); letter-spacing: 0.06em; line-height: 1; text-shadow: 0 2px 10px rgba(0,0,0,0.5); }
  .headline--lead { left: 612px; top: 70px; font-size: 40px; font-weight: 700; }
  .headline--course { left: 530px; top: 90px; font-size: 76px; }
  .headline--price { left: 340px; top: 160px; font-size: 76px; letter-spacing: 0.16em; }

  .feature-row { position: absolute; left: 52px; top: 704px; width: 740px; display: flex; justify-content: space-between; }
  .feature { width: 232px; }
  .feature__photo { width: 232px; height: 150px; }
  .feature__photo--room { background: linear-gradient(135deg, #4a4540, #2a2725 60%, #6b604f); }
  .feature__photo--beef { background: linear-gradient(135deg, #7a3b36, #b06a5c 50%, #3c2a25); }
  .feature__photo--drinks { background: linear-gradient(135deg, #3a2a1c, #b0722e 50%, #2a2220); }
  .feature__caption {
    margin-top: 18px; text-align: center; color: var(--gold); font-size: 18px; line-height: 1.7; letter-spacing: 0.12em;
    border-top: 1px solid var(--line); border-bottom: 1px solid var(--line); padding: 6px 0;
  }

  .shop-info { position: absolute; left: 52px; top: 975px; width: 380px; color: var(--gold); }
  .shop-info__label { font-size: 15px; letter-spacing: 0.1em; }
  .shop-info__name { font-size: 24px; font-weight: 700; letter-spacing: 0.08em; margin: 2px 0 12px; padding-bottom: 8px; border-bottom: 1px solid var(--line); }
  .shop-info__row { font-size: 14px; line-height: 1.9; letter-spacing: 0.04em; }

  .course-box { position: absolute; left: 450px; top: 972px; width: 342px; padding: 10px 0; border: 1px solid var(--line); text-align: center; color: var(--gold); }
  .course-box__title { font-size: 16px; line-height: 1.5; letter-spacing: 0.12em; margin-bottom: 4px; }
  .course-box__list { list-style: none; font-size: 15px; line-height: 1.35; letter-spacing: 0.1em; }
</style>
</head>
<body>
<main class="flyer">
  <div class="hero-photo" role="img" aria-label="炙った黒毛和牛の肉寿司が並ぶ写真"></div>

  <h1 class="headline headline--lead">チラシ持参で</h1>
  <p class="headline headline--course">お試しコース</p>
  <p class="headline headline--price">980円</p>

  <section class="feature-row">
    <div class="feature">
      <div class="feature__photo feature__photo--room" role="img" aria-label="落ち着いた照明の店内写真"></div>
      <p class="feature__caption">高級感漂う<br>ラグジュアリー空間</p>
    </div>
    <div class="feature">
      <div class="feature__photo feature__photo--beef" role="img" aria-label="黒毛和牛の盛り合わせ写真"></div>
      <p class="feature__caption">厳選された<br>黒毛和牛</p>
    </div>
    <div class="feature">
      <div class="feature__photo feature__photo--drinks" role="img" aria-label="カクテルとボトルが並ぶバーカウンターの写真"></div>
      <p class="feature__caption">時間を気にせず<br>お楽しみください</p>
    </div>
  </section>

  <section class="shop-info">
    <p class="shop-info__label">焼肉バー</p>
    <p class="shop-info__name">焼肉BAR MIYOKO</p>
    <p class="shop-info__row">所在地：名古屋市中区栄見5-2-14 灯火ビル3F</p>
    <p class="shop-info__row">営業時間：[月〜土]18:00〜翌5:00(L.O.翌4:00)</p>
    <p class="shop-info__row">電話番号：052-731-4806</p>
  </section>

  <section class="course-box">
    <p class="course-box__title">＜お試しコースの内容＞</p>
    <ul class="course-box__list">
      <li>厚切り牛タン塩</li>
      <li>黒毛和牛カルビ</li>
      <li>MIYOKOサラダ</li>
      <li>本日の赤身</li>
      <li>特選ロース</li>
      <li>テールの土鍋蒸し</li>
      <li>和牛ホルモン</li>
      <li>ライス</li>
    </ul>
  </section>
</main>
</body>
</html>
```